Ridgeline Talent Associates Business Card Design

We need a business card design for our new company - Ridgeline Talent Associates. RLTA is a recruitment firm that focuses on recruiting engineers and geologist for mid-size oil and gas companies. We would like our logo on the business card, which is attached, and we would like the color scheme on business cards to coordinate with our logo.

Industry/Entity Type

Oil And Gas

Contact Information for Business Card

Dana Whitlow, Founder and Managing Partner, dmw@ridgelinetalentco.org, 888.507.3942 (work), 5730915.0600 (cell), 573.642.1907 (fax), www.ridgelinetalentco.org

```html
<!DOCTYPE html>
<html lang="en">
<head>
<meta charset="utf-8">
<title>Ridgeline Talent Associates — Business Card</title>
<link rel="stylesheet" href="https://fonts.googleapis.com/css2?family=Open+Sans:wght@400;600&display=swap">
<style>
  :root {
    --bg: #eceef0;
    --card: #ffffff;
    --navy: #1d3a7a;
    --navy-deep: #15295a;
    --band-top: #2f4f96;
    --band-bottom: #1a3270;
    --rule: #2a2a2a;
    --ink: #111111;
  }
  * { margin: 0; padding: 0; box-sizing: border-box; }
  html, body {
    width: 1200px;
    height: 600px;
    overflow: hidden;
    background: var(--bg);
    font-family: "Open Sans", Arial, sans-serif;
  }
  .canvas {
    position: relative;
    width: 1200px;
    height: 600px;
  }
  .card {
    position: absolute;
    top: 152px;
    width: 467px;
    height: 278px;
    background: var(--card);
    border-radius: 16px;
    overflow: hidden;
    box-shadow: 0 2px 10px rgba(0, 0, 0, 0.08);
  }
  .card--front { left: 93px; }
  .card--back { left: 638px; }

  .brand {
    display: flex;
    align-items: center;
    gap: 10px;
    color: var(--navy);
    font-weight: 600;
    white-space: nowrap;
  }
  .brand__dot {
    border-radius: 50%;
    background: var(--navy);
    flex: none;
  }

  .card--front .brand {
    position: absolute;
    left: 0;
    right: 0;
    top: 124px;
    justify-content: center;
    font-size: 21px;
    letter-spacing: 0.3px;
  }
  .card--front .brand__dot { width: 22px; height: 22px; }

  .card--back .brand {
    position: absolute;
    left: 22px;
    top: 72px;
    font-size: 15px;
  }
  .card--back .brand__dot { width: 16px; height: 16px; }

  .person {
    position: absolute;
    left: 22px;
    top: 126px;
  }
  .person__name {
    color: var(--navy-deep);
    font-size: 14.5px;
    font-weight: 400;
    line-height: 18px;
  }
  .person__title {
    color: var(--ink);
    font-size: 11.5px;
    line-height: 15px;
  }
  .contact {
    position: absolute;
    left: 22px;
    top: 168px;
    list-style: none;
    font-size: 11.5px;
    line-height: 14.6px;
    color: var(--ink);
  }
  .contact__label { color: var(--navy-deep); }
  .website {
    position: absolute;
    left: 22px;
    top: 231px;
    font-size: 11.5px;
    color: var(--navy-deep);
  }
  .band {
    position: absolute;
    left: 0;
    right: 0;
    bottom: 0;
    height: 26px;
    border-top: 2px solid var(--rule);
    background: linear-gradient(to bottom, var(--band-top), var(--band-bottom));
  }
</style>
</head>
<body>
  <main class="canvas">
    <section class="card card--front" aria-label="Card front">
      <div class="brand">
        <span class="brand__dot"></span>
        <span class="brand__name">Ridgeline Talent Associates</span>
      </div>
    </section>

    <section class="card card--back" aria-label="Card back">
      <div class="brand">
        <span class="brand__dot"></span>
        <span class="brand__name">Ridgeline Talent Associates</span>
      </div>

      <div class="person">
        <p class="person__name">Dana Whitlow</p>
        <p class="person__title">Founder and Managing Partner</p>
      </div>

      <ul class="contact">
        <li><span class="contact__label">Office:</span> 888.507.3942</li>
        <li><span class="contact__label">Fax:</span> 573.642.1907</li>
        <li><span class="contact__label">Mobile:</span> 5730915.0600</li>
        <li><span class="contact__label">Email:</span> dmw@ridgelinetalentco.org</li>
      </ul>

      <p class="website">www.ridgelinetalentco.org</p>

      <div class="band"></div>
    </section>
  </main>
</body>
</html>
```